Medical Cannabis company is looking for a LOGO design *

SILVER PETALWORKS (SP) is a new company in the Israeli medical cannabis industry. We will engage in PREMIUM medical cannabis growing and cultivation and also manufacturing of HIGH-END cannabis based medical products.
the design should reflect luxury, high-end and Pharma-grade products.
the design should use color GOLD and NOT using the famous cannabis leaf !

Target Market(s)

international medical cannabis Pharmaceutical companies
and of course local and international patients

Contact Information for Business Card

Yoav Ben-Ami
Founder and CEO

Silver Petalworks
Medical grade cannabis

yoavbenami@mailnest.example
972-52-3186907

Colors
ffc214
fbed22

Requirements
Must have
• clean and simple
• luxury
• gold !!
• (can also have green for Cannabis and/or blue for Pharma)
Should not have
• cannabis leaf

```html
<!DOCTYPE html>
<html lang="en">
<head>
<meta charset="utf-8">
<title>Silver Petalworks — Business Card</title>
<link rel="stylesheet" href="https://fonts.googleapis.com/css2?family=Karla:wght@400;500;700&display=swap">
<style>
  :root {
    --gold-deep: #fbb324;
    --gold-bright: #fbed22;
    --paper: #ffffff;
    --ink-grey: #555555;
    --backdrop: #ecebe8;
  }
  html, body {
    margin: 0;
    padding: 0;
    width: 1200px;
    height: 1200px;
    overflow: hidden;
    background: var(--backdrop);
    font-family: "Karla", sans-serif;
  }
  .canvas {
    position: relative;
    width: 1200px;
    height: 1200px;
  }
  .card {
    position: absolute;
    left: 150px;
    width: 900px;
    height: 500px;
    background: var(--paper);
    box-shadow: 0 6px 18px rgba(0,0,0,0.12);
  }
  .card svg { display: block; width: 100%; height: 100%; }
  .card--front { top: 70px; }
  .card--back { top: 630px; }

  .brand-name {
    font-family: "Karla", sans-serif;
    font-weight: 700;
    font-size: 40px;
    letter-spacing: 1px;
    fill: var(--gold-deep);
  }
  .brand-tagline {
    font-family: "Karla", sans-serif;
    font-weight: 400;
    font-size: 24px;
    letter-spacing: 6px;
    fill: var(--ink-grey);
  }
  .person-name {
    font-family: "Karla", sans-serif;
    font-weight: 700;
    font-size: 36px;
    fill: var(--gold-deep);
  }
  .person-title {
    font-family: "Karla", sans-serif;
    font-weight: 400;
    font-size: 25px;
    fill: var(--ink-grey);
  }
  .contact-line {
    font-family: "Karla", sans-serif;
    font-weight: 400;
    font-size: 25px;
    fill: var(--ink-grey);
  }
  .band-deep { fill: var(--gold-deep); }
  .band-bright { fill: var(--gold-bright); }
  .field-paper { fill: var(--paper); }
  .icon { fill: var(--gold-deep); }
</style>
</head>
<body>
<main class="canvas">

  <section class="card card--front" aria-label="Business card front">
    <svg viewBox="0 0 900 500" xmlns="http://www.w3.org/2000/svg">
      <rect class="band-deep" x="0" y="0" width="900" height="500"/>
      <path class="band-bright" d="M 185 0 L 285 0 C 215 130, 215 330, 255 500 C 195 350, 170 160, 185 0 Z"/>
      <path class="field-paper" d="M 500 0 C 390 120, 345 320, 350 500 L 900 500 L 900 0 Z"/>
      <text class="brand-name" x="855" y="395" text-anchor="end">SILVER PETALWORKS</text>
      <text class="brand-tagline" x="855" y="437" text-anchor="end">medical grade cannabis</text>
    </svg>
  </section>

  <section class="card card--back" aria-label="Business card back">
    <svg viewBox="0 0 900 500" xmlns="http://www.w3.org/2000/svg">
      <path class="band-bright" d="M 680 0 L 755 0 C 745 250, 580 410, 290 500 C 520 390, 665 250, 680 0 Z"/>
      <text class="person-name" x="55" y="408">Yoav Ben-Ami</text>
      <text class="person-title" x="55" y="448">Founder and CEO</text>

      <text class="contact-line" x="825" y="408" text-anchor="end">972-52-3186907</text>
      <path class="icon" transform="translate(836,390) scale(0.9)"
            d="M4 1 L8 1 L10 6 L7.5 8 C9 11 11 13 14 14.5 L16 12 L21 14 L21 18 C21 19.5 19.5 21 18 20.5 C9 18.5 3.5 13 1.5 4 C1 2.5 2.5 1 4 1 Z"/>

      <text class="contact-line" x="825" y="448" text-anchor="end">yoavbenami@mailnest.example</text>
      <g class="icon" transform="translate(836,433)">
        <rect x="0" y="0" width="20" height="14" rx="1"/>
        <path d="M1 1.5 L10 8 L19 1.5" fill="none" stroke="#ffffff" stroke-width="1.6"/>
      </g>
    </svg>
  </section>

</main>
</body>
</html>
```